Professionelles Social Media Material für Reinigungsdienstleister
Zielgruppe
Wir reinigen Privathaushalte, Ferienwohnungen, Arztpraxen und Büroräume.
Aufgabenstellung
Ich wünsche Material für ein professionelles Auftreten bei Facebook und Instagram. Wir müssen bei Facebook leider neu starten und haben Instagram bei dieser Firma bisher vernachlässigt.
Nun wollen wir unser Social Media professionell erscheinen lassen und einen Plan für die kommenden 2 Monate erstellen. Wir suchen dafür mindestens 20 passende Postings und die Inhalte für den Start.
Nachtrag zu den Postings: Wir wollen ganz allgemeinen Content und sind offen für alle Vorschläge. Es kann gern auch eine Sommeraktion beworben werden, bei der wir Neukunden 100€ schenken und eine Aktion, bei der es eine kostenlose Erstreinigung gibt um unsere Leistung zu testen.

```html
<!DOCTYPE html>
<html lang="de">
<head>
<meta charset="utf-8">
<title>Wohnglanz Pilot – Social Media Postings Reinigungsservice</title>
<link href="https://fonts.googleapis.com/css2?family=Rubik:ital,wght@0,400;0,500;0,700;0,800;1,500;1,700;1,800&display=swap" rel="stylesheet">
<style>
  :root{
    --page:#dcdcdc;
    --paper:#ffffff;
    --blue:#75a7c9;
    --blue-soft:#d9eaf6;
    --blue-text:#2f6fb5;
    --blue-deep:#4f7fa8;
    --navy:#4a5a86;
    --yellow:#f5df5a;
    --white:#ffffff;
  }
  *{box-sizing:border-box;margin:0;padding:0}
  html,body{width:741px;height:1200px;overflow:hidden;background:var(--page)}
  body{position:relative;font-family:"Rubik",sans-serif}

  .post{position:absolute;width:194px;height:245px;background:var(--paper);overflow:hidden;
    box-shadow:2px 3px 5px rgba(0,0,0,.18)}
  .abs{position:absolute}

  .header{position:absolute;left:46px;top:0;width:148px;height:70px;background:var(--blue);
    border-bottom-left-radius:50px 62px}
  .title{position:absolute;left:69px;top:13px;color:var(--white);font-weight:800;font-size:16px;line-height:16px;letter-spacing:.2px}

  .brand{position:absolute;left:4px;top:7px;width:40px;text-align:center;color:var(--navy);font-weight:700;font-size:6.4px;line-height:7.6px}
  .brand-dot{display:block;width:13px;height:13px;border-radius:50%;background:var(--navy);margin:0 auto 3px}

  .pill{position:absolute;background:var(--yellow);border-radius:50%;}
  .pill-text{position:absolute;color:var(--blue-text);font-style:italic;font-weight:800;font-size:10px;line-height:10.5px}

  .soft{position:absolute;background:var(--blue-soft);border-radius:50%}
  .band{position:absolute;left:-10px;width:214px;background:var(--blue);border-radius:55% 45% 0 0 / 22px 18px 0 0}
  .band-text{position:absolute;color:var(--white);font-size:7.4px;line-height:10px;font-weight:500}
  .band-text b{font-weight:700}
  .band-text.italic{font-style:italic}

  .photo{position:absolute;border-radius:44px;border:3px solid var(--white)}
  .bubble{position:absolute;left:0;top:0}
  .quote{position:absolute;color:var(--blue);font-weight:800;font-style:italic;font-size:34px;line-height:34px}
  .body-text{position:absolute;color:var(--blue);font-size:7.6px;line-height:10.3px}
  .body-text b{color:var(--blue-text);font-weight:700}
  .icon-label{position:absolute;color:var(--blue-text);font-size:5.4px}
</style>
</head>
<body>

<!-- 1 Helden -->
<section class="post" style="left:46px;top:59px">
  <div class="header"></div><h2 class="title">REINIGUNGS<br>SERVICE</h2>
  <div class="brand"><span class="brand-dot"></span>Wohnglanz<br>Pilot</div>
  <div class="soft" style="left:-20px;top:75px;width:110px;height:110px"></div>
  <div class="band" style="top:160px;height:90px"></div>
  <div class="pill" style="left:38px;top:62px;width:150px;height:44px;transform:rotate(-4deg)"></div>
  <p class="pill-text" style="left:68px;top:78px">Sauberkeit ist unsere<br>Leidenschaft</p>
  <div class="abs" role="img" aria-label="Foto einer fliegenden Reinigungsheldin mit Maske und buntem Staubwedel" style="left:22px;top:98px;width:172px;height:100px;border-radius:50px;background:radial-gradient(circle at 45% 45%,#e8c9b5 0 18%,#c7464f 19% 32%,#f0b7c9 33% 55%,rgba(240,200,220,0) 70%)"></div>
  <p class="abs" style="left:12px;top:104px;color:var(--blue-text);font-style:italic;font-size:7px;line-height:8.5px;transform:rotate(-14deg)">Jetzt<br>Angebot<br>einholen!</p>
  <p class="band-text" style="left:36px;top:200px;font-size:6.6px;line-height:8.8px">Das bisschen<br>Haushalt macht sich von allein …<br>Du brauchst nur den <b><i>richtigen Helden!</i></b></p>
</section>

<!-- 2 Team -->
<section class="post" style="left:274px;top:59px">
  <div class="header"></div><h2 class="title">REINIGUNGS<br>SERVICE</h2>
  <div class="brand"><span class="brand-dot"></span>Wohnglanz<br>Pilot</div>
  <div class="soft" style="left:-30px;top:80px;width:150px;height:110px"></div>
  <div class="pill" style="left:36px;top:68px;width:150px;height:42px"></div>
  <div class="band" style="top:158px;height:92px"></div>
  <div class="soft" style="left:40px;top:150px;width:130px;height:28px;border-radius:50%"></div>
  <div class="abs" role="img" aria-label="Foto von drei Reinigungskräften in blauen Schürzen mit Staubsauger und Putzmitteln" style="left:72px;top:34px;width:122px;height:150px;border-radius:30px 30px 12px 12px;background:linear-gradient(180deg,#e8d4c8 0%,#5d8fbf 35%,#3f6f9f 70%,#e6c44b 100%)"></div>
  <p class="abs" style="left:17px;top:114px;color:var(--blue-deep);font-style:italic;font-weight:500;font-size:8px;line-height:10.5px">Zuverlässig,<br>pünktlich und<br>blitzsauber</p>
  <p class="band-text italic" style="left:37px;top:200px;font-style:italic">Wir sorgen für glanzvolle Ergebnisse<br>in privaten <b>Haushalten, Büros</b><br><b>und Gewerbe.</b></p>
</section>

<!-- 3 Sommeraktion -->
<section class="post" style="left:501px;top:59px">
  <div class="header"></div><h2 class="title">REINIGUNGS<br>SERVICE</h2>
  <div class="brand"><span class="brand-dot"></span>Wohnglanz<br>Pilot</div>
  <div class="band" style="top:140px;height:110px"></div>
  <div class="pill" style="left:38px;top:62px;width:150px;height:34px"></div>
  <p class="pill-text" style="left:68px;top:73px;font-size:12px">Sommeraktion!</p>
  <div class="photo" role="img" aria-label="Foto einer überraschten Frau vor Strand und blauem Himmel" style="left:9px;top:96px;width:180px;height:98px;background:linear-gradient(160deg,#bcd7ec 0%,#e9f2f8 45%,#d8c7a8 100%)"></div>
  <p class="abs" style="left:96px;top:108px;color:var(--blue-text);font-weight:700;font-style:italic;font-size:6.8px;line-height:7.5px;transform:rotate(-14deg)">Jeder<br>Neukunde<br>bekommt:</p>
  <p class="abs" style="left:100px;top:132px;color:var(--blue-text);font-weight:800;font-style:italic;font-size:9.5px;line-height:11px;transform:rotate(-14deg)">€ 100,-<br>GESCHENKT!</p>
  <p class="band-text italic" style="left:36px;top:204px;font-style:italic">Damit du entspanntin den Urlaub<br>fahren kannst!</p>
</section>

<!-- 4 Checkliste -->
<section class="post" style="left:46px;top:331px">
  <div class="header"></div><h2 class="title">REINIGUNGS<br>SERVICE</h2>
  <div class="brand"><span class="brand-dot"></span>Wohnglanz<br>Pilot</div>
  <div class="soft" style="left:-20px;top:75px;width:100px;height:110px"></div>
  <div class="pill" style="left:38px;top:66px;width:150px;height:40px"></div>
  <p class="pill-text" style="left:66px;top:77px">Checkliste:<br>&nbsp;&nbsp;&nbsp;&nbsp;Frühjahrsputz</p>
  <div class="abs" style="left:4px;top:100px;width:118px;height:82px;border-radius:50%;background:var(--blue)"></div>
  <p class="abs" style="left:39px;top:110px;color:var(--white);font-size:7px;line-height:8.6px">Dinge, die beim<br>Frühjahrsputz<br>oft vergessen<br>werden …</p>
  <p class="abs" style="left:39px;top:152px;color:var(--white);font-size:8.4px;line-height:9.4px">Wir vergessen<br>nichts!</p>
  <svg class="abs" style="left:0;top:0" width="194" height="245" viewBox="0 0 194 245" fill="none" stroke="#75a7c9" stroke-width="1.3">
    <path d="M118 133 L135 128 M122 158 L138 155 M100 175 L108 180 M20 180 L24 198" stroke-width="0.7"/>
    <rect x="139" y="113" width="14" height="3" rx="1.5"/><rect x="139" y="119" width="14" height="3" rx="1.5"/><rect x="139" y="125" width="14" height="3" rx="1.5"/><rect x="139" y="131" width="14" height="3" rx="1.5"/>
    <rect x="140" y="150" width="13" height="24"/><path d="M146.5 150 V174 M140 162 H153"/>
    <rect x="26" y="188" width="6" height="22" rx="3"/><path d="M32 193 H44"/>
    <rect x="103" y="193" width="11" height="14" rx="2"/><rect x="107" y="197" width="3" height="6"/>
  </svg>
  <p class="icon-label" style="left:137px;top:138px">Heizkörper</p>
  <p class="icon-label" style="left:137px;top:181px">Fensterrahmen</p>
  <p class="icon-label" style="left:47px;top:195px">Türgriffe</p>
  <p class="icon-label" style="left:119px;top:195px">Lichtschalter</p>
  <div class="band" style="top:213px;height:40px;border-radius:0"></div>
  <p class="band-text italic" style="left:35px;top:225px;font-style:italic">Jetzt Angebot einholen!</p>
</section>

<!-- 5 Glas -->
<section class="post" style="left:274px;top:331px">
  <div class="header"></div><h2 class="title">REINIGUNGS<br>SERVICE</h2>
  <div class="brand"><span class="brand-dot"></span>Wohnglanz<br>Pilot</div>
  <div class="band" style="top:150px;height:100px"></div>
  <div class="pill" style="left:38px;top:62px;width:150px;height:42px"></div>
  <p class="pill-text" style="left:82px;top:72px">Glas- und<br>Fensterreinigung</p>
  <div class="photo" role="img" aria-label="Foto eines Mannes beim Reinigen einer großen Glasscheibe" style="left:8px;top:103px;width:180px;height:96px;background:linear-gradient(135deg,#cfe4f3 0%,#9fc6e3 55%,#3d4a57 100%)"></div>
  <div class="abs" style="left:8px;top:101px;width:58px;height:14px;background:var(--blue);border-radius:4px;transform:rotate(-14deg)"></div>
  <p class="abs" style="left:18px;top:96px;color:var(--white);font-style:italic;font-size:7px;line-height:6.5px;transform:rotate(-14deg)">garantiert<br><span style="font-size:5px">streifenfrei</span></p>
  <p class="band-text" style="left:45px;top:206px">Wir bringen Ihre Fenster<br>zum Strahlen!</p>
</section>

<!-- 6 Kunden -->
<section class="post" style="left:501px;top:331px">
  <div class="header"></div><h2 class="title">REINIGUNGS<br>SERVICE</h2>
  <div class="brand"><span class="brand-dot"></span>Wohnglanz<br>Pilot</div>
  <div class="soft" style="left:-22px;top:70px;width:92px;height:150px"></div>
  <div class="pill" style="left:38px;top:62px;width:150px;height:40px"></div>
  <p class="pill-text" style="left:68px;top:83px">was Kunden sagen:</p>
  <svg class="bubble" width="194" height="245" viewBox="0 0 194 245"><path d="M92 106 H194 V198 H96 Q72 198 64 204 L44 226 L54 194 Q38 180 38 152 Q38 106 92 106Z" fill="#fff" stroke="#d9eaf6" stroke-width="2"/></svg>
  <p class="quote" style="left:24px;top:112px">"</p>
  <p class="body-text" style="left:68px;top:132px"><b><i>„Zuverlässig, pünktlich<br>und blitzsauber –</i></b><br>ich empfehle euch gerne<br>weiter!“ – Karin Brandt<br>Wir sagen:<br>Danke für das Vertrauen!</p>
</section>

<!-- 7 Erstreinigung -->
<section class="post" style="left:46px;top:624px">
  <div class="header"></div><h2 class="title">REINIGUNGS<br>SERVICE</h2>
  <div class="brand"><span class="brand-dot"></span>Wohnglanz<br>Pilot</div>
  <div class="band" style="top:158px;height:92px"></div>
  <div class="pill" style="left:38px;top:62px;width:150px;height:40px"></div>
  <p class="abs" style="left:68px;top:74px;color:var(--blue-text);font-size:7.8px;line-height:9px">Wir <b>schenken</b> dir<br>die Erstreinigung</p>
  <div class="photo" role="img" aria-label="Foto einer lachenden Frau mit rosa Putzhandschuhen vor türkisem Hintergrund" style="left:8px;top:102px;width:180px;height:94px;background:linear-gradient(90deg,#6fa7b3 0%,#73aab5 55%,#e9b83d 80%,#6fa7b3 100%)"></div>
  <p class="abs" style="left:28px;top:138px;color:var(--white);font-weight:800;font-size:13px">TESTE UNS!</p>
  <p class="band-text" style="left:55px;top:213px">Erstreinigung gratis · <b>Jetzt<br>Angebot einholen!</b></p>
</section>

<!-- 8 Stellen -->
<section class="post" style="left:274px;top:624px">
  <div class="header"></div><h2 class="title">REINIGUNGS<br>SERVICE</h2>
  <div class="brand"><span class="brand-dot"></span>Wohnglanz<br>Pilot</div>
  <div class="soft" style="left:-22px;top:70px;width:92px;height:150px"></div>
  <div class="pill" style="left:38px;top:60px;width:150px;height:40px"></div>
  <p class="pill-text" style="left:69px;top:82px">WIR STELLEN EIN!</p>
  <svg class="bubble" width="194" height="245" viewBox="0 0 194 245"><path d="M92 108 H194 V202 H96 Q72 202 64 208 L40 228 L54 198 Q38 184 38 156 Q38 108 92 108Z" fill="#fff" stroke="#d9eaf6" stroke-width="2"/></svg>
  <p class="quote" style="left:22px;top:112px">"</p>
  <p class="body-text" style="left:68px;top:126px">Wir suchen Verstärkung!<br>(m/w/d) <b>in Teilzeit<br>gesucht – fair bezahlt,<br>familiäres Team.</b><br>Sende uns deine<br>Bewerbung per Mail<br>oder ruf an!</p>
</section>

<!-- 9 Büro -->
<section class="post" style="left:501px;top:624px">
  <div class="header"></div><h2 class="title">REINIGUNGS<br>SERVICE</h2>
  <div class="brand"><span class="brand-dot"></span>Wohnglanz<br>Pilot</div>
  <div class="band" style="top:150px;height:100px"></div>
  <div class="pill" style="left:38px;top:62px;width:150px;height:40px"></div>
  <p class="abs" style="left:98px;top:71px;color:var(--blue-text);font-weight:700;font-size:9.5px">Büroreinigung</p>
  <p class="abs" style="left:98px;top:84px;color:var(--blue-text);font-weight:700;font-style:italic;font-size:5.4px">warum sie so wichtig ist</p>
  <div class="photo" role="img" aria-label="Foto einer Frau, die sich im hellen Büro am Schreibtisch streckt" style="left:8px;top:98px;width:180px;height:90px;background:linear-gradient(90deg,#c8d3dc 0%,#eef2f4 40%,#c6783d 55%,#eef2f4 70%,#a9b8c3 100%)"></div>
  <div class="abs" style="left:131px;top:109px;width:57px;height:57px;border-radius:50%;background:var(--blue);border:2px solid var(--white)"></div>
  <p class="abs" style="left:134px;top:123px;width:51px;text-align:center;color:var(--white);font-size:4.2px;line-height:5.4px">Wussten Sie, dass <b>saubere Arbeitsplätze</b> die <b>Produktivität</b> um 12 % steigern können?“</p>
  <p class="band-text" style="left:52px;top:203px">Jetzt Reinigungsplan für Ihr<br>Büro erstellen lassen.</p>
</section>

<!-- 10 Spezial -->
<section class="post" style="left:46px;top:895px">
  <div class="header"></div><h2 class="title">REINIGUNGS<br>SERVICE</h2>
  <div class="brand"><span class="brand-dot"></span>Wohnglanz<br>Pilot</div>
  <div class="pill" style="left:38px;top:64px;width:150px;height:40px"></div>
  <p class="pill-text" style="left:68px;top:82px">Spezialreinigung</p>
  <div class="band" style="top:200px;height:50px;border-radius:0"></div>
  <div class="photo" role="img" aria-label="Foto einer gefliesten Dusche mit gelber Quietscheente" style="left:8px;top:104px;width:180px;height:94px;background:linear-gradient(180deg,#1f6f9f 0%,#3a8fbd 55%,#e7eef3 90%)"></div>
  <p class="abs" style="left:66px;top:114px;color:var(--white);font-weight:500;font-size:8.6px;line-height:10.5px;text-align:center">Schimmel in<br>der Dusche?</p>
  <div class="abs" style="left:16px;top:150px;width:78px;height:40px;border-radius:50%;background:var(--blue-soft);transform:rotate(-6deg)"></div>
  <p class="abs" style="left:18px;top:158px;color:var(--blue-text);font-size:4.6px;line-height:5.6px;transform:rotate(-6deg)"><b>Kein Problem.</b> Wir über-<br>nehmen auch schwierige<br>Fälle – professionell und<br>hygienisch.“</p>
  <p class="band-text" style="left:37px;top:217px">Jetzt Angebot einholen!</p>
</section>

<!-- 11 Umzug -->
<section class="post" style="left:274px;top:895px">
  <div class="header"></div><h2 class="title">REINIGUNGS<br>SERVICE</h2>
  <div class="brand"><span class="brand-dot"></span>Wohnglanz<br>Pilot</div>
  <div class="soft" style="left:-25px;top:75px;width:160px;height:120px"></div>
  <div class="band" style="top:150px;height:100px"></div>
  <div class="pill" style="left:38px;top:62px;width:150px;height:40px"></div>
  <p class="abs" style="left:68px;top:74px;color:var(--blue-text);font-weight:700;font-size:9.6px;line-height:10px">Umzugsreinigung,<br>Endreinigung</p>
  <div class="abs" role="img" aria-label="Foto von Umzugskartons mit Besen, Teppich und Putzutensilien" style="left:74px;top:108px;width:106px;height:88px;border-radius:8px;background:linear-gradient(180deg,#c79d6f 0%,#b98b5c 60%,#8fae7d 100%)"></div>
  <p class="abs" style="left:23px;top:117px;color:var(--blue-deep);font-size:6.4px;line-height:10px">Neuer Mieter,<br>neuer Glanz!</p>
  <p class="band-text" style="left:37px;top:206px;font-size:5px;line-height:7px">Wir übernehmen die Endreinigung beim Umzug –<br>zuverlässig und gründlich.</p>
  <p class="band-text" style="left:37px;top:224px;font-weight:700">Jetzt Angebot einholen!</p>
</section>

<!-- 12 Umfrage -->
<section class="post" style="left:501px;top:895px">
  <div class="header"></div><h2 class="title">REINIGUNGS<br>SERVICE</h2>
  <div class="brand"><span class="brand-dot"></span>Wohnglanz<br>Pilot</div>
  <div class="soft" style="left:-22px;top:70px;width:92px;height:150px"></div>
  <div class="pill" style="left:38px;top:62px;width:150px;height:40px"></div>
  <p class="pill-text" style="left:68px;top:78px;font-size:12px">Umfrage</p>
  <svg class="bubble" width="194" height="245" viewBox="0 0 194 245"><path d="M92 106 H194 V206 H96 Q72 206 64 212 L42 228 L54 202 Q38 188 38 158 Q38 106 92 106Z" fill="#fff" stroke="#d9eaf6" stroke-width="2"/></svg>
  <p class="quote" style="left:24px;top:112px">"</p>
  <p class="abs" style="left:68px;top:129px;color:var(--blue-text);font-weight:700;font-size:8.6px;line-height:9.6px">Was ist für Sie<br>wichtiger?</p>
  <p class="abs" style="left:68px;top:155px;color:var(--blue-text);font-weight:500;font-size:7.8px;line-height:12px">A) Zeitersparnis<br>B) Hygiene<br>C) Umweltfreundlichkeit<br>&nbsp;&nbsp;&nbsp;&nbsp;&nbsp;<b>Kommentieren Sie!</b></p>
</section>

</body>
</html>
```